pet sitting business brochure

please create a professional bold brochure for my new pet sitting business
please use my logo and collect suitable photos online to go with design of brochure
my colour theme is orange and blue
please look at my website to collect information
www.brindlepawminders.com.au

Reason: extended until tomorrow to make any changes to designs

```html
<!DOCTYPE html>
<html lang="en">
<head>
<meta charset="utf-8">
<title>Pet Sitting Brochure</title>
<link href="https://fonts.googleapis.com/css2?family=Roboto+Slab:wght@700&family=Open+Sans:wght@400;600;700&display=swap" rel="stylesheet">
<style>
  :root {
    --bg: #8e8e8e;
    --navy: #1c3b7a;
    --orange: #f08a1c;
    --sky: #2fa0e0;
    --paper: #ececec;
    --white: #ffffff;
    --ink: #5a5a5a;
  }
  html, body { margin: 0; padding: 0; overflow: hidden; }
  body {
    width: 1200px; height: 899px;
    background: var(--bg);
    font-family: "Open Sans", Arial, sans-serif;
    position: relative;
  }
  .brochure {
    position: absolute; left: 60px; top: 90px;
    width: 1080px; height: 720px;
    display: flex;
    box-shadow: 0 10px 30px rgba(0,0,0,.3);
  }
  .panel { width: 360px; height: 720px; position: relative; overflow: hidden; }
  .panel svg { position: absolute; inset: 0; }

  /* left panel */
  .panel-intro { background: var(--paper); }
  .section-title {
    font-family: "Roboto Slab", Georgia, serif;
    font-weight: 700; font-size: 22px; letter-spacing: 1px;
    color: var(--orange); margin: 0 0 12px;
  }
  .intro { padding: 48px 34px 24px; }
  .body-text { font-size: 13.5px; line-height: 1.6; color: var(--ink); margin: 0; }
  .feature {
    background: var(--orange); color: var(--white);
    padding: 22px 34px; margin: 6px 0 26px;
  }
  .feature p { margin: 0; font-size: 13.5px; line-height: 1.6; font-weight: 600; }
  .feature strong { font-family: "Roboto Slab", Georgia, serif; letter-spacing: .5px; }
  .about { padding: 0 34px; }

  /* right panel */
  .panel-services { background: var(--navy); }
  .services {
    position: absolute; left: 40px; right: 22px; top: 390px;
    color: var(--white);
  }
  .services .section-title { font-size: 24px; margin-bottom: 16px; }
  .service-list { list-style: none; margin: 0; padding: 0; }
  .service-list li { font-size: 14.5px; line-height: 1.5; font-weight: 600; margin-bottom: 6px; }
  .service-name { color: var(--orange); font-weight: 700; }
</style>
</head>
<body>
  <div class="brochure">
    <section class="panel panel-intro">
      <div class="intro">
        <h2 class="section-title">INTRODUCTION</h2>
        <p class="body-text">We are a locally owned pet care service offering loving, reliable visits while you are away. We feed, walk, play and care for dogs, cats, birds, rabbits, horses and fish, so your pets stay happy and safe at home.</p>
      </div>
      <div class="feature">
        <p><strong>DOG WALKING</strong> Your dog will be walked at times that suit your routine, with plenty of exercise, fresh air and play. Every walk ends with fresh water, a quick brush and a happy, tired dog ready to rest.</p>
      </div>
      <div class="about">
        <h2 class="section-title">ABOUT US</h2>
        <p class="body-text">Hi, I am a fully qualified animal technician with many years of experience caring for all kinds of pets. I hold a Diploma in Animal Science and love meeting new animals and their families. If you are looking for a pet sitter to look after your pets in the comfort of your own home, I would love to help.</p>
      </div>
    </section>

    <section class="panel panel-photos">
      <svg width="360" height="720" viewBox="0 0 360 720">
        <defs>
          <linearGradient id="dogTone" x1="0" y1="0" x2="1" y2="1">
            <stop offset="0" stop-color="#f3ede6"/>
            <stop offset=".5" stop-color="#d9a75f"/>
            <stop offset="1" stop-color="#b9804a"/>
          </linearGradient>
          <linearGradient id="walkTone" x1="0" y1="0" x2="0" y2="1">
            <stop offset="0" stop-color="#9bbf6a"/>
            <stop offset=".6" stop-color="#7b8f5a"/>
            <stop offset="1" stop-color="#c9c4b8"/>
          </linearGradient>
        </defs>
        <rect class="panel-base" width="360" height="720" fill="var(--navy)"/>
        <path class="light-field" d="M0 0 H360 V250 C360 330 320 360 260 360 H0 Z" fill="var(--white)"/>
        <path class="stripe-sky" d="M318 0 V250 C318 320 290 345 240 350" fill="none" stroke="var(--sky)" stroke-width="12"/>
        <path class="stripe-orange" d="M340 0 V255 C340 345 300 372 240 374" fill="none" stroke="var(--orange)" stroke-width="10"/>
        <path role="img" aria-label="Photo of a smiling golden retriever lying beside its owner" d="M0 20 H280 Q300 20 300 40 V240 C300 300 275 330 225 330 H0 Z" fill="url(#dogTone)"/>
        <line class="dash-line" x1="20" y1="395" x2="340" y2="395" stroke="var(--orange)" stroke-width="4" stroke-dasharray="14 12"/>
        <rect x="30" y="425" width="290" height="270" rx="26" fill="var(--white)"/>
        <rect role="img" aria-label="Photo of a woman jogging outdoors with her dog" x="38" y="433" width="274" height="254" rx="20" fill="url(#walkTone)"/>
      </svg>
    </section>

    <section class="panel panel-services">
      <svg width="360" height="720" viewBox="0 0 360 720">
        <defs>
          <linearGradient id="horseTone" x1="0" y1="0" x2="1" y2="1">
            <stop offset="0" stop-color="#e9e4dc"/>
            <stop offset=".55" stop-color="#8a5a3a"/>
            <stop offset="1" stop-color="#5b3a26"/>
          </linearGradient>
        </defs>
        <path class="stripe-sky" d="M0 20 C30 60 40 120 40 200 V330" fill="none" stroke="var(--sky)" stroke-width="10"/>
        <path class="stripe-orange" d="M0 60 C18 100 22 150 22 210 V360" fill="none" stroke="var(--orange)" stroke-width="10"/>
        <rect x="88" y="28" width="256" height="300" rx="26" fill="var(--white)"/>
        <rect role="img" aria-label="Photo of a brown horse wearing a halter" x="96" y="36" width="240" height="284" rx="20" fill="url(#horseTone)"/>
      </svg>
      <div class="services">
        <h2 class="section-title">ADDITIONAL SERVICES</h2>
        <ul class="service-list">
          <li><span class="service-name">Horses Rugged</span> : Price charged on number of horses and ease of catching</li>
          <li><span class="service-name">Plants Watered</span> : Price charged on number of plants and time spent.</li>
          <li><span class="service-name">Medicine Administered</span> : charged daily</li>
        </ul>
      </div>
    </section>
  </div>
</body>
</html>
```